Design business card for Bright Harbour Coaching!

I am a personal development coach (like a life coach) and corporate trainer and need a professionally designed double sided business card.

It needs to contain the business logo (I'm happy for the designer to choose the layout of the logo as I am still working out the best option myself) and the following information:

Corinne Vashti
Personal Development Coach and Trainer

+61 (0)452 918 637 (written that way)
corinne@bright-harbour.example

www.bright-harbour.example

```html
<!DOCTYPE html>
<html lang="en">
<head>
<meta charset="utf-8">
<title>Bright Harbour Coaching – Business Card</title>
<link rel="stylesheet" href="https://fonts.googleapis.com/css2?family=Open+Sans:wght@400;600&display=swap">
<style>
  :root {
    --backdrop: #3a3431;
    --card: #1b1b1c;
    --card-edge: #262627;
    --brand-grey: #8a8a8c;
    --teal: #1f8f9b;
    --contact: #e6e6e6;
    --divider: #cfcfcf;
  }
  * { margin: 0; padding: 0; box-sizing: border-box; }
  html, body {
    width: 1200px;
    height: 814px;
    overflow: hidden;
    background: var(--backdrop);
    font-family: "Open Sans", Arial, sans-serif;
  }
  .canvas {
    width: 1200px;
    height: 814px;
    display: flex;
    align-items: center;
    justify-content: center;
    gap: 60px;
  }
  .card {
    width: 510px;
    height: 310px;
    background: var(--card);
    border: 1px solid var(--card-edge);
    border-radius: 3px;
    box-shadow: 0 14px 30px rgba(0,0,0,0.45);
    position: relative;
  }
  .brand {
    display: flex;
    align-items: center;
    gap: 12px;
  }
  .brand-dot {
    width: 30px;
    height: 30px;
    border-radius: 50%;
  }
  .brand-name {
    font-weight: 400;
    text-transform: uppercase;
    letter-spacing: 1px;
    line-height: 1;
    color: var(--brand-grey);
  }

  /* Front */
  .card-front { display: flex; align-items: center; justify-content: center; }
  .card-front .brand-dot { background: var(--brand-grey); }
  .card-front .brand-name { font-size: 24px; color: #b9b9bb; }

  /* Back */
  .card-back .brand {
    position: absolute;
    top: 74px;
    left: 60px;
  }
  .card-back .brand-dot { background: var(--teal); width: 40px; height: 40px; }
  .card-back .brand-name { font-size: 23px; }

  .details {
    position: absolute;
    top: 178px;
    left: 36px;
    display: flex;
    align-items: flex-start;
  }
  .person {
    text-align: right;
    padding-right: 14px;
    color: var(--teal);
  }
  .person-name { font-size: 17px; font-weight: 600; margin-bottom: 4px; }
  .person-role { font-size: 12.5px; line-height: 1.35; }
  .divider {
    width: 1px;
    height: 64px;
    background: var(--divider);
    margin-top: 30px;
  }
  .contact {
    list-style: none;
    padding-left: 14px;
    margin-top: 34px;
    color: var(--contact);
    font-size: 13.5px;
    line-height: 1.45;
  }
</style>
</head>
<body>
  <main class="canvas">
    <section class="card card-front" aria-label="Card front">
      <div class="brand">
        <span class="brand-dot"></span>
        <span class="brand-name">Bright Harbour Coaching</span>
      </div>
    </section>

    <section class="card card-back" aria-label="Card back">
      <div class="brand">
        <span class="brand-dot"></span>
        <span class="brand-name">Bright Harbour Coaching</span>
      </div>
      <div class="details">
        <div class="person">
          <p class="person-name">Corinne Vashti</p>
          <p class="person-role">Personal Development<br>Coach &amp; Trainer</p>
        </div>
        <span class="divider"></span>
        <ul class="contact">
          <li>+61 (0)452 918 637</li>
          <li>corinne@bright-harbour.example</li>
          <li>www.bright-harbour.example</li>
        </ul>
      </div>
    </section>
  </main>
</body>
</html>
```